Einladungskarten für Der Helle Bogen
Designer hat mehrere Vorschläge entwickelt und Änderungen super schnell umgesetzt. Wir waren sehr zufrieden und freuen uns auf unsere diesjährige Einladungskarte.
Zielgruppe
Wir sind ein Tochterunternehmen von Harting Verlag. Wir sind 'Der Helle Bogen' , Holding der Radio Stationen/Beteiligungen und möchten alle Geschäftsführer/innen der Beteiligungen, einige Politiker und Medienräte zu einem Event einladen.
Aufgabenstellung
Wir hätten gerne eine quadratische Karte.
Das Event heißt 'Ortsabend 2023'
Termin 03.07.2023 um 19 Uhr
Anmeldung bis spätestens 23.06.2022 an events@heller-bogen.de
Diese Karte gilt als Eintrittskarte
Adresse: KAIHALLE, Lindenweg 52, 90461 Nürnberg
Dresscode: Business Casual
Firmenfarben: Blau: RGB 23/110/182 und Grau: RGB 134/135/135
Firmenschriftart: Century Gothic

```html
<!DOCTYPE html>
<html lang="de">
<head>
<meta charset="utf-8">
<title>Ortsabend 2023 – Einladung</title>
<link rel="stylesheet" href="https://fonts.googleapis.com/css2?family=Dancing+Script:wght@500&family=Rock+Salt&display=swap">
<style>
  :root {
    --stone-light: #fbfbfb;
    --stone-mid: #e9e9ea;
    --stone-vein: #d4d5d7;
    --ink: #141414;
    --leaf-dark: #3f5a2c;
    --leaf-mid: #7d9a4f;
    --water: #c9d3d6;
    --canopy: #f1f1ef;
  }
  * { margin: 0; padding: 0; box-sizing: border-box; }
  html, body { width: 1200px; height: 1200px; overflow: hidden; }
  body {
    position: relative;
    background:
      radial-gradient(ellipse at 20% 30%, var(--stone-mid) 0%, transparent 45%),
      radial-gradient(ellipse at 80% 70%, var(--stone-vein) 0%, transparent 40%),
      radial-gradient(ellipse at 70% 15%, var(--stone-mid) 0%, transparent 35%),
      linear-gradient(135deg, var(--stone-light), var(--stone-mid) 60%, var(--stone-light));
    color: var(--ink);
  }
  .surface { position: absolute; inset: 0; }

  .event-title {
    position: absolute;
    font-family: "Rock Salt", cursive;
    color: var(--ink);
    line-height: 1;
    white-space: nowrap;
  }
  .event-title__name {
    left: 118px;
    top: 190px;
    font-size: 88px;
    transform: rotate(-20deg);
    transform-origin: left bottom;
  }
  .event-title__year {
    left: 650px;
    top: 90px;
    font-size: 120px;
    letter-spacing: 6px;
    transform: rotate(14deg);
    transform-origin: left top;
  }

  .venue-photo {
    position: absolute;
    left: 297px;
    top: 300px;
    width: 612px;
    height: 565px;
    background:
      linear-gradient(180deg, var(--canopy) 0%, var(--canopy) 22%, var(--leaf-mid) 36%, var(--water) 48%, #9aa3a4 62%, var(--leaf-mid) 78%, var(--leaf-dark) 100%);
    clip-path: polygon(0% 6%, 4% 4%, 10% 5%, 16% 2%, 24% 3%, 40% 3%, 60% 2%, 80% 3%, 92% 2%, 100% 4%,
      100% 100%, 90% 98%, 80% 99%, 72% 97%, 64% 99%, 56% 97%, 48% 99%, 38% 98%, 28% 99%, 18% 98%, 8% 100%, 0% 98%);
  }

  .event-details {
    position: absolute;
    left: 0;
    right: 0;
    top: 888px;
    text-align: center;
    font-family: "Dancing Script", cursive;
    font-weight: 500;
    font-size: 29px;
    line-height: 51px;
    color: var(--ink);
  }
</style>
</head>
<body>
  <div class="surface" role="img" aria-label="Heller Marmoruntergrund mit grauen Adern"></div>

  <h1 class="event-title event-title__name">Ortsabend</h1>
  <div class="event-title event-title__year">2023</div>

  <div class="venue-photo" role="img" aria-label="Foto einer Seeterrasse mit weißen Sonnenschirmen, Stühlen und blühenden Pflanzen im Vordergrund"></div>

  <div class="event-details">
    <p>Termin 03.07.2023 um 19 Uhr</p>
    <p>Anmeldung bis spätestens 23.06.2022 an events@heller-bogen.de</p>
    <p>Diese Karte gilt als Eintrittskarte</p>
    <p>Adresse: KAIHALLE, Lindenweg 52, 90461 Nürnberg</p>
    <p>Dresscode: Business Casual</p>
  </div>
</body>
</html>
```